KORVEL Flyer

We need a flyer for the research project called 'KORVEL'. We will distribute this flyer during conferences and events to our audience (mainly industry (Security and IoT), medical organisations, and researchers) in order to provide the basic information about the project.
The project will provide a Holistic Network Guard Framework for the Health-Care Industry.
We are attaching files to provide with concrete information on our requirements:
- KORVEL brochure content_final.ppt: includes the content we would like to include in the flyer. There is also the URL to the project website
- KORVEL layout.doc: it includes information about the layout (example video from another project brochure)
- KORVEL logo final version_sourcefile.zip: the project logo
- Logo-partners.zip: Logos that will be included (please follow the numbered order.)
We would like to use colors that belong to the project logo color range. Regarding the images that you may include in the brochure we wouldn't like to propose any because we do not want to limitate your imagination. They could be relevant to medical devices, security, etc.

```html
<!DOCTYPE html>
<html lang="en">
<head>
<meta charset="utf-8">
<title>KORVEL Flyer</title>
<link href="https://fonts.googleapis.com/css2?family=Exo+2:wght@600;700;800&family=Montserrat:wght@400;600;700&display=swap" rel="stylesheet">
<style>
  :root {
    --teal: #12b2a5;
    --teal-deep: #0d978c;
    --teal-line: #34c7ba;
    --accent: #1fc6b6;
    --ink-dark: #17191b;
    --ink-mid: #24282b;
    --white: #ffffff;
    --paper: #eef1f2;
    --grey-text: #4a4f52;
  }
  * { box-sizing: border-box; margin: 0; padding: 0; }
  html, body { width: 1200px; height: 900px; overflow: hidden; }
  body {
    background: var(--paper);
    font-family: "Montserrat", sans-serif;
    color: var(--white);
    position: relative;
  }
  .spread {
    position: absolute;
    left: 20px;
    width: 1160px;
    height: 410px;
    display: grid;
    grid-template-columns: repeat(4, 290px);
    box-shadow: 0 6px 18px rgba(0,0,0,0.12);
  }
  .spread--inside { top: 25px; }
  .spread--outside { top: 465px; }
  .panel { position: relative; height: 410px; padding: 22px 20px; overflow: hidden; }
  .panel--teal { background: var(--teal); }
  .panel--white { background: var(--white); color: var(--grey-text); }
  .panel--dark { background: var(--ink-dark); }

  h2, h3, h4 { font-family: "Exo 2", sans-serif; }
  p, li { font-size: 7.6px; line-height: 1.45; }
  .brand { font-weight: 700; }

  /* inside spread */
  .connectors { position: absolute; left: 0; top: 0; width: 870px; height: 410px; pointer-events: none; }
  .topic { position: relative; padding-left: 8px; border-left: 2px solid var(--white); margin-bottom: 34px; }
  .topic h3 { font-size: 13.5px; font-weight: 700; margin-bottom: 6px; }
  .topic p { text-align: justify; }
  .topic--indent { margin-left: 12px; }
  .why-title { text-align: center; font-size: 14px; font-weight: 700; line-height: 1.25; margin-top: 4px; }
  .why-title u { text-decoration-thickness: 1.5px; }
  .emblem {
    width: 120px; height: 120px; border-radius: 50%;
    background: var(--white);
    margin: 26px auto 0;
    display: flex; align-items: center; justify-content: center;
    font-family: "Exo 2", sans-serif; font-weight: 700; font-size: 19px; color: var(--teal-deep);
    position: relative; z-index: 1;
  }
  .panel--center .topic { position: absolute; left: 20px; right: 20px; bottom: 8px; margin: 0; }
  .panel-body { position: relative; z-index: 1; }

  .partners-title { font-family: "Exo 2", sans-serif; font-size: 13px; font-weight: 700; color: var(--teal); text-align: center; margin-bottom: 26px; }
  .partner-grid { display: grid; grid-template-columns: repeat(3, 1fr); gap: 16px 14px; padding: 0 18px; }
  .partner-badge { height: 20px; background: #d5dcde; border-radius: 3px; }
  .partner-badge--round { width: 26px; height: 26px; border-radius: 50%; justify-self: center; }
  .funding { position: absolute; left: 20px; right: 16px; bottom: 24px; display: flex; gap: 8px; align-items: flex-start; }
  .funding-badge { width: 34px; height: 24px; background: #1f3f93; flex: none; }
  .funding p { font-size: 5.6px; line-height: 1.4; color: var(--grey-text); }

  /* outside spread */
  .dark-photo { position: absolute; inset: 0; background: linear-gradient(160deg, #2b3134 0%, #15181a 55%, #1f2527 100%); }
  .dark-content { position: relative; z-index: 1; }
  .pilot-title { font-family: "Exo 2", sans-serif; font-size: 24px; font-weight: 800; color: var(--accent); text-align: center; margin-bottom: 12px; }
  .dark-head { font-family: "Exo 2", sans-serif; font-size: 12px; font-weight: 700; color: var(--accent); text-align: center; margin: 12px 0 5px; }
  .dark-content p, .dark-content li { text-align: center; list-style: none; color: #e6ecec; }

  .involve-title { font-size: 13px; font-weight: 700; text-align: center; line-height: 1.25; margin-top: 22px; }
  .involve-lead { text-align: center; margin-top: 6px; }
  .how-title { font-family: "Exo 2", sans-serif; font-size: 12px; font-weight: 700; text-align: center; margin: 14px 0 5px; }
  .how-list { list-style: none; text-align: center; }
  .social { display: grid; grid-template-columns: 1fr 1fr; gap: 10px 10px; margin-top: 30px; padding: 0 6px; }
  .social-item { display: flex; align-items: center; gap: 6px; font-size: 7.6px; }
  .social-dot { width: 10px; height: 10px; background: var(--white); border-radius: 2px; flex: none; }
  .site-link { grid-column: 1 / -1; justify-content: center; }

  .cover-top { display: flex; justify-content: space-between; align-items: flex-start; }
  .cover-keywords { list-style: none; text-align: right; border-right: 1.5px solid var(--white); padding-right: 8px; }
  .cover-keywords li { font-size: 7px; line-height: 1.5; }
  .wordmark { display: flex; align-items: center; gap: 6px; font-family: "Montserrat", sans-serif; font-weight: 600; font-size: 17px; letter-spacing: 1px; margin-top: 6px; }
  .wordmark-circle { width: 18px; height: 18px; border: 2px solid var(--white); border-radius: 50%; }
  .cover-title { font-family: "Exo 2", sans-serif; font-weight: 800; font-size: 21px; line-height: 1.1; margin-top: 90px; letter-spacing: 0.5px; }
  .cover-title span { display: block; font-size: 12.5px; margin-top: 3px; }
  .cover-url { position: absolute; right: 20px; bottom: 14px; font-size: 7.5px; }

  .what-title { font-family: "Exo 2", sans-serif; font-size: 14px; font-weight: 700; color: var(--accent); margin-bottom: 14px; }
  .what-block { border-left: 2px solid var(--accent); padding-left: 8px; margin-bottom: 16px; }
  .what-block h4 { font-size: 10px; font-weight: 700; color: var(--accent); margin-bottom: 4px; }
  .what-block p, .what-block li { text-align: left; }
  .what-block ul { list-style: none; }
  .what-block li::before { content: "• "; }
</style>
</head>
<body>

<section class="spread spread--inside">
  <svg class="connectors" viewBox="0 0 870 410" aria-hidden="true">
    <g stroke="#0d978c" stroke-width="2.5" fill="none">
      <polyline points="435,175 330,175 300,120 250,120"/>
      <polyline points="435,175 300,240 250,240"/>
      <polyline points="435,175 380,300 330,360"/>
      <polyline points="435,175 540,175 570,120 610,120"/>
      <polyline points="435,175 560,240 610,240"/>
      <polyline points="435,175 490,300 540,330"/>
      <polyline points="435,175 435,330"/>
    </g>
  </svg>

  <article class="panel panel--teal">
    <div class="panel-body">
      <div class="topic">
        <h3>Industry (Security and IoT)</h3>
        <p><span class="brand">KORVEL</span> will provide tools to evaluate healthcare devices and services and receive a detailed compliance and certification report that assesses if the device or service is vulnerable and/or misused, or if its attack surface doesn't implement crucial security requirements.</p>
      </div>
      <div class="topic topic--indent">
        <h3>Medical organisations</h3>
        <p>The <span class="brand">KORVEL ecosystem</span> will armour medical organisations from multiple cybersecurity threats and will therefore protect patient data. It will provide the means for medical organisations to become aware and understand the cybersecurity risks to their cyber-physical security and Privacy Policy and to make informed decisions to choose the use of KORVEL certified devices.</p>
      </div>
      <div class="topic topic--indent">
        <h3>Society</h3>
        <p><span class="brand">KORVEL</span> will give patients the strong feeling that their data are secure. It will help patients increase their control over their multiple IoT devices, because they will be able to choose those devices available in the market based on whether they are KORVEL certified or not.</p>
      </div>
    </div>
  </article>

  <article class="panel panel--teal panel--center">
    <div class="panel-body">
      <h2 class="why-title">Why KORVEL is<br><u>important</u> for you?</h2>
      <div class="emblem">KORVEL</div>
    </div>
    <div class="topic">
      <h3>Research</h3>
      <p>Through the extensive research of this Research and Innovation project, KORVEL will produce research articles and technical demonstrations at journals and conferences, as well as a community of developers and scientists.</p>
    </div>
  </article>

  <article class="panel panel--teal">
    <div class="panel-body">
      <div class="topic">
        <h3>Policy</h3>
        <p><span class="brand">KORVEL</span> will investigate improvements and alternatives to current institutional and governance frameworks in order to improve cybersecurity awareness and stimulate the usage of the proposed solution, aiming to empower patient data privacy.</p>
      </div>
      <div class="topic">
        <h3>International networks</h3>
        <p>Through international networks, KORVEL will increase awareness to several stakeholders about the project's achievements. KORVEL will seek opportunities to participate in relevant activities organised by the international network. In addition, international networks will be requested to share online information published by KORVEL, through their communication channels, e.g. websites and social networks.</p>
      </div>
      <div class="topic">
        <h3>Related EU-funded projects</h3>
        <p>By cooperating with <span class="brand">KORVEL</span>, other EU-funded projects can develop more impactful and sustainable cybersecurity environments in the health sector, and enhance their ability to Disseminate and Communicate their results.</p>
      </div>
    </div>
  </article>

  <article class="panel panel--white">
    <h2 class="partners-title">KORVEL partners</h2>
    <div class="partner-grid" aria-label="Partner badges">
      <div class="partner-badge"></div><div class="partner-badge partner-badge--round"></div><div class="partner-badge"></div>
      <div class="partner-badge"></div><div class="partner-badge"></div><div class="partner-badge" style="visibility:hidden"></div>
      <div class="partner-badge"></div><div class="partner-badge partner-badge--round"></div><div class="partner-badge"></div>
      <div class="partner-badge"></div><div class="partner-badge"></div><div class="partner-badge" style="visibility:hidden"></div>
      <div class="partner-badge"></div><div class="partner-badge partner-badge--round"></div><div class="partner-badge"></div>
      <div class="partner-badge partner-badge--round"></div><div class="partner-badge"></div><div class="partner-badge"></div>
    </div>
    <div class="funding">
      <div class="funding-badge"></div>
      <div>
        <p>This project has received funding from a European research and innovation programme under a grant agreement.</p>
        <p>Digital Society, Trust and Cyber Security in E-Health.</p>
      </div>
    </div>
  </article>
</section>

<section class="spread spread--outside">
  <article class="panel panel--dark">
    <div class="dark-photo" role="img" aria-label="Dimly lit server room with rows of racks"></div>
    <div class="dark-content">
      <h2 class="pilot-title">Pilot</h2>
      <h3 class="dark-head">Did you know that</h3>
      <p>The project's pilots will deploy and evaluate the KORVEL solution at business as usual and emergency situations across various use cases at three different countries.</p>
      <h3 class="dark-head">Where?</h3>
      <ul>
        <li>• Hospital Vale Sereno in Portugal</li>
        <li>• Hospital Stellara Medical in Romania</li>
        <li>• The Meridia Regional Health Authority in Greece</li>
      </ul>
      <h3 class="dark-head">How?</h3>
      <p>The overall solution will be evaluated using Key Performance Indicators related with the KORVEL cyber-security effectiveness usability and cost-effectiveness, by end-users, project partners and business stakeholders.</p>
    </div>
  </article>

  <article class="panel panel--teal">
    <h2 class="involve-title">Get involved in our project<br>activities!</h2>
    <p class="involve-lead">Participate in the KORVEL yearly workshops and organized events and activities.</p>
    <h3 class="how-title">How?</h3>
    <ul class="how-list">
      <li>• Visit our website https://korvel-project.eu/ and join our community</li>
      <li>• Join our social media channels</li>
      <li>• Subscribe to our Newsletter</li>
      <li>• Check our upcoming events to participate</li>
    </ul>
    <div class="social">
      <div class="social-item"><span class="social-dot"></span>@ProjectKorvel</div>
      <div class="social-item"><span class="social-dot"></span>korvel-project.eu</div>
      <div class="social-item"><span class="social-dot"></span>korvel-project</div>
      <div class="social-item"><span class="social-dot"></span>The korvel project eu</div>
      <div class="social-item site-link"><span class="social-dot"></span>https://korvel-project.eu/</div>
    </div>
  </article>

  <article class="panel panel--teal">
    <div class="cover-top">
      <ul class="cover-keywords">
        <li>• Healthcare Services</li>
        <li>• Medical &amp; Health Devices</li>
        <li>• Cybersecurity</li>
        <li>• Data privacy</li>
        <li>• Cybersecurity Vulnerability<br>Assessment and Certification</li>
      </ul>
      <div class="wordmark"><span class="wordmark-circle"></span>KORVEL</div>
    </div>
    <h1 class="cover-title">A Holistic<br>Network Guard Framework<span>for the Health-Care Industry</span></h1>
    <p class="cover-url">korvel-project.eu</p>
  </article>

  <article class="panel panel--dark">
    <div class="dark-photo" role="img" aria-label="Dimly lit server room with rows of racks"></div>
    <div class="dark-content">
      <h2 class="what-title">What is KORVEL ?</h2>
      <div class="what-block">
        <h4>The Challenge</h4>
        <p>Solving the Riddle of Cyber-Security protection in Healthcare IT ecosystems.</p>
      </div>
      <div class="what-block">
        <h4>How does KORVEL tackle the challenge?</h4>
        <p>Through:</p>
        <ul>
          <li>Cyber protection and data privacy and integrity</li>
          <li>The proactive assessment &amp; mitigation of Cyber-Security threats</li>
          <li>Evaluation and verification of new Medical Devices and Services</li>
          <li>Providing the KORVEL Certification</li>
          <li>Near real time vulnerability assessment of operating IT Ecosystems</li>
        </ul>
      </div>
      <div class="what-block">
        <h4>Pilot</h4>
        <p>The KORVEL proposed technology and business framework will be demonstrated and validated under realistic operating conditions and various use case scenarios.</p>
      </div>
    </div>
  </article>
</section>

</body>
</html>
```